Custom Seed Packet design for Flower Farm

We need a design for our seeds packets.
The design will be a kind of "fill in the blanks" as we need the design to be adaptable for multiple varieties of seed. We will be using the design for a rubber stamp.
Our seed packets are 90x90mm in size.
Black logo only. No colour required.
A vintage botanical influence is desired.
Will need to include the following info,
"Lantern Wick Co logo" , "Seeds", "Plant Type", "Variety", "Harvested"

```html
<!DOCTYPE html>
<html lang="en">
<head>
<meta charset="utf-8">
<title>Seed Packet – Lantern Wick Co. Flower Farm</title>
<link rel="stylesheet" href="https://fonts.googleapis.com/css2?family=Barlow:wght@600&family=Marcellus&display=swap">
<style>
  :root {
    --page: #ffffff;
    --kraft-dark: #c9a763;
    --kraft-mid: #d3b577;
    --kraft-light: #e2cc9b;
    --ink: #3a3a3a;
    --ink-strong: #1e1e1e;
    --botanical-tint: rgba(120, 100, 70, 0.10);
  }
  * { margin: 0; padding: 0; box-sizing: border-box; }
  html, body {
    width: 1200px;
    height: 1200px;
    overflow: hidden;
    background: var(--page);
  }
  .canvas {
    position: relative;
    width: 1200px;
    height: 1200px;
  }
  .packet {
    position: absolute;
    left: 119px;
    top: 119px;
    width: 953px;
    height: 953px;
    background: linear-gradient(135deg, var(--kraft-dark) 0%, var(--kraft-mid) 45%, var(--kraft-light) 100%);
    box-shadow: 0 2px 6px rgba(0, 0, 0, 0.18);
  }
  .packet__frame {
    position: absolute;
    left: 34px;
    top: 34px;
    width: 886px;
    height: 886px;
    border: 6px solid var(--ink);
  }
  .botanical {
    position: absolute;
    background: radial-gradient(ellipse at 50% 40%, var(--botanical-tint), rgba(120, 100, 70, 0) 70%);
  }
  .botanical--right { left: 520px; top: 330px; width: 400px; height: 590px; }
  .botanical--left { left: 50px; top: 620px; width: 210px; height: 300px; }
  .title {
    position: absolute;
    left: 0;
    top: 0;
    width: 953px;
    height: 320px;
  }
  .title text {
    font-family: "Marcellus", "Times New Roman", serif;
    font-size: 296px;
    fill: var(--ink);
  }
  .field {
    position: absolute;
    left: 91px;
    width: 772px;
  }
  .field__label {
    display: block;
    font-family: "Barlow", Arial, sans-serif;
    font-weight: 600;
    font-size: 19px;
    line-height: 22px;
    color: var(--ink-strong);
    margin-bottom: 10px;
    padding-left: 2px;
  }
  .field__box {
    height: 78px;
    border: 2px solid var(--ink-strong);
  }
  .field--plant { top: 318px; }
  .field--variety { top: 455px; }
  .field--harvested { top: 593px; }
  .brand {
    position: absolute;
    left: 0;
    top: 720px;
    width: 953px;
    text-align: center;
    font-family: "Barlow", Arial, sans-serif;
    font-weight: 600;
    font-size: 22px;
    line-height: 28px;
    color: var(--ink-strong);
  }
  .brand__dot {
    display: block;
    width: 46px;
    height: 46px;
    margin: 0 auto 14px;
    border-radius: 50%;
    background: var(--ink-strong);
  }
</style>
</head>
<body>
<div class="canvas">
  <div class="packet">
    <div class="botanical botanical--right" role="img" aria-label="Faint line drawing of poppy flowers on tall stems"></div>
    <div class="botanical botanical--left" role="img" aria-label="Faint line drawing of a small poppy cluster"></div>
    <div class="packet__frame"></div>

    <svg class="title" viewBox="0 0 953 320" aria-label="Seed">
      <defs>
        <path id="title-arc" d="M 85 283 Q 476 243 869 283"/>
      </defs>
      <text>
        <textPath href="#title-arc" textLength="784" lengthAdjust="spacingAndGlyphs">SEED</textPath>
      </text>
    </svg>

    <div class="field field--plant">
      <span class="field__label">Plant Type</span>
      <div class="field__box"></div>
    </div>
    <div class="field field--variety">
      <span class="field__label">Variety</span>
      <div class="field__box"></div>
    </div>
    <div class="field field--harvested">
      <span class="field__label">Harvested</span>
      <div class="field__box"></div>
    </div>

    <div class="brand">
      <span class="brand__dot"></span>
      Lantern Wick Co.<br>Flower Farm
    </div>
  </div>
</div>
</body>
</html>
```